business card for law firm that reflects the web site -www.MarlaQuentby.com. That is pleasant to read

We need a business card for a small law firm. Your company designed our logo - tree of life - which I can provide to the designers. The card should be on both sides. Use the coloring from the web site (www.MarlaQuentby.com) and logo (I have several formats). I am attaching the logo, but not sure what format to use.

First side name of firm: Law Office of M.K. Quentby, P.A. 4819 West Pallisor, Suite 300, Phoenix, AZ 85016, Phone: 602.555.3841, Fax: 602.555.7290, web site: www.MarlaQuentby.com, email: MQuentby@MarlaQuentby.com.
Marla K. Quentby Bankruptcy and Foreclosure Attorney & Counselor.
Back side (perhaps vertical) the logo and then Notes with lines. At the bottom: Proud to help people and small businesses file for bankruptcy protection. We are a debt relief agency.
Updates

I have several versions of the logo. Will be happy to share whatever you need. Added Sunday, April 3, 2016

Target Market(s)

everyone

Industry/Entity Type

Legal

Contact Information for Business Card

I prefer something unique (rounded edges, design that adopts my web site - www.MarlaQuentby.com.

Font styles to use
Serif

Requirements
Must have
• First side name of firm: Law Office of M.K. Quentby, P.A. 4819 West Pallisor, Suite 300, Phoenix, AZ 85016, Phone: 602.555.3841, Fax: 602.555.7290, web site: www.MarlaQuentby.com, email: MQuentby@MarlaQuentby.com.
• Marla K. Quentby Bankruptcy and Foreclosure Attorney & Counselor.
• Back side (perhaps vertical) the logo and then Notes with lines. At the bottom: Proud to help people and small businesses file for bankruptcy protection. We are a debt relief agency.
• Green and brown colors that reflect the web site: www.MarlaQuentby.com
Should not have
• Type so small that older people cannot read.

```html
<!DOCTYPE html>
<html lang="en">
<head>
<meta charset="utf-8">
<title>Law Office of M.K. Quentby, P.A. — Business Card</title>
<link rel="stylesheet" href="https://fonts.googleapis.com/css2?family=Cinzel:wght@500;600&family=Source+Sans+3:ital,wght@0,400;0,600;1,400&display=swap">
<style>
  :root {
    --backdrop: #e8e5e0;
    --paper: #ffffff;
    --brown: #3a2218;
    --brown-text: #4a2a1e;
    --green: #1c3320;
    --green-text: #1f3a22;
    --grey-text: #5e5e5e;
    --rule: #d6d6d6;
    --faint: #f1f1f1;
  }
  * { margin: 0; padding: 0; box-sizing: border-box; }
  html, body {
    width: 1200px; height: 1000px; overflow: hidden;
    background: var(--backdrop);
    font-family: "Source Sans 3", "Myriad Pro", Arial, sans-serif;
  }
  .canvas { position: relative; width: 1200px; height: 1000px; }

  .card { position: absolute; background: var(--paper); overflow: hidden; }

  /* Back side */
  .card-back { left: 80px; top: 90px; width: 467px; height: 818px; border: 1px solid #d9d6d1; }
  .card-back .tree-faint {
    position: absolute; left: 130px; top: 340px; width: 337px; height: 478px;
    background: radial-gradient(ellipse at 55% 35%, var(--faint) 0%, #f6f6f6 50%, rgba(255,255,255,0) 75%);
  }
  .card-back .badge { position: absolute; left: 110px; top: 97px; }
  .notes { position: absolute; left: 36px; top: 434px; width: 404px; }
  .notes-label { font-size: 17px; color: var(--grey-text); line-height: 22px; }
  .notes-line { height: 53px; border-bottom: 1px solid var(--rule); }
  .notes-line:first-of-type { height: 11px; }
  .tagline {
    position: absolute; left: 0; right: 0; top: 733px;
    text-align: center; font-style: italic; font-size: 17.5px; line-height: 24px;
    color: var(--green-text);
  }

  /* Front side */
  .card-front { left: 344px; top: 270px; width: 809px; height: 460px; border: 1px solid #d9d6d1; }
  .band-top { position: absolute; left: 0; top: 0; width: 100%; height: 22px; background: var(--brown); }
  .band-bottom { position: absolute; left: 0; bottom: 0; width: 100%; height: 23px; background: var(--green); }
  .card-front .badge { position: absolute; left: 38px; top: 102px; }
  .divider { position: absolute; left: 326px; top: 110px; width: 1px; height: 240px;
    background: linear-gradient(to bottom, rgba(0,0,0,0), #dcdcdc 20%, #dcdcdc 80%, rgba(0,0,0,0)); }
  .tree-illustration {
    position: absolute; right: 0; bottom: 23px; width: 165px; height: 285px;
    background: radial-gradient(ellipse at 60% 30%, #2c4a2e 0%, #3d5e3f 40%, rgba(61,94,63,0.35) 65%, rgba(255,255,255,0) 78%);
  }
  .contact { position: absolute; left: 362px; top: 96px; color: var(--grey-text); }
  .attorney-name {
    font-family: "Cinzel", "Trajan Pro", Georgia, serif; font-weight: 600;
    font-size: 25px; letter-spacing: 1px; color: var(--green-text); line-height: 30px;
  }
  .attorney-title { font-size: 17px; line-height: 22px; margin-top: 2px; }
  .firm-name { font-weight: 600; font-size: 17px; color: var(--brown-text); margin-top: 24px; line-height: 22px; }
  .address { font-size: 17px; line-height: 23px; }
  .contact-list { list-style: none; margin-top: 10px; }
  .contact-list li { display: flex; align-items: center; height: 29px; font-size: 17px; }
  .contact-list svg { width: 14px; height: 14px; margin-right: 12px; fill: var(--brown); flex: none; }

  .badge-name { font-family: "Cinzel", Georgia, serif; font-weight: 600; fill: var(--brown); }
</style>
</head>
<body>
<main class="canvas">

  <section class="card card-back" aria-label="Business card, back side">
    <div class="tree-faint" role="img" aria-label="Faint tree illustration in the background"></div>
    <svg class="badge" width="236" height="236" viewBox="0 0 236 236" aria-label="M.K. Quentby">
      <circle cx="118" cy="118" r="114" fill="none" stroke="var(--brown)" stroke-width="5"/>
      <text class="badge-name" x="118" y="126" text-anchor="middle" font-size="24">M.K. Quentby</text>
    </svg>
    <div class="notes">
      <p class="notes-label">Notes:</p>
      <div class="notes-line"></div>
      <div class="notes-line"></div>
      <div class="notes-line"></div>
      <div class="notes-line"></div>
    </div>
    <p class="tagline">Proud to help people and small businesses file<br>for bankruptcy protection.</p>
  </section>

  <section class="card card-front" aria-label="Business card, front side">
    <div class="band-top"></div>
    <svg class="badge" width="252" height="252" viewBox="0 0 252 252" aria-label="M.K. Quentby">
      <circle cx="126" cy="126" r="122" fill="none" stroke="var(--brown)" stroke-width="5"/>
      <text class="badge-name" x="126" y="134" text-anchor="middle" font-size="26">M.K. Quentby</text>
    </svg>
    <div class="divider"></div>
    <div class="contact">
      <h1 class="attorney-name">Marla K. Quentby</h1>
      <p class="attorney-title">Bankruptcy and Foreclosure Attorney &amp; Counselor</p>
      <p class="firm-name">Law Office of M.K. Quentby</p>
      <p class="address">P.A. 4819 West Pallisor, Suite 300,<br>Phoenix, AZ 85016</p>
      <ul class="contact-list">
        <li><svg viewBox="0 0 16 16" aria-label="Phone"><path d="M3.6 1l2.5 3.3-1.5 1.6c.9 2 2.6 3.7 4.6 4.6l1.6-1.5L14 11.5 12.6 14C6.8 14 2 9.2 2 3.4z"/></svg>602.555.3841</li>
        <li><svg viewBox="0 0 16 16" aria-label="Fax"><path d="M4 1h8v4H4zM1 6h14v7h-3v2H4v-2H1zm4 5v3h6v-3z"/></svg>602.555.7290</li>
        <li><svg viewBox="0 0 16 16" aria-label="Email"><path d="M1 3h14v10H1zm1.5 1.2L8 8.6l5.5-4.4z"/></svg>MQuentby@MarlaQuentby.com</li>
        <li><svg viewBox="0 0 16 16" aria-label="Website"><circle cx="8" cy="8" r="6.5" fill="none" stroke="var(--brown)" stroke-width="1.4"/><path d="M1.5 8h13M8 1.5c-3 3.5-3 9.5 0 13M8 1.5c3 3.5 3 9.5 0 13" fill="none" stroke="var(--brown)" stroke-width="1.2"/></svg>www.MarlaQuentby.com</li>
      </ul>
    </div>
    <div class="tree-illustration" role="img" aria-label="Dark green tree illustration growing from the bottom edge"></div>
    <div class="band-bottom"></div>
  </section>

</main>
</body>
</html>
```